Medien Firma benötigt Briefpapier
Zielgruppe
Firma:
Wir sind im Bereich Veranstaltungstechnik und Eventmanagement seit 2007 tätig. Ab 2009 konnten wir unsere Expertise um die Bereiche Medientechnik und TV Produktion erweitern. Durch dieses Portfolio sind wir in der Lage, alle Facetten der technischen Planung durchzuführen.
Bereiche:
Veranstaltungstechnik - Medientechnik - Livestreaming
Kunden:
B2B
Aufgabenstellung
Erstellung von Briefpapier mit dem vorhandenen Logo.
Das Briefpapier soll auch als Produktsheet nutzbar sein. Also muss der Footer Text austauschbar sein.
Schlicht, Modern, Zeitlos, max. zwei Farben

```html
<!DOCTYPE html>
<html lang="de">
<head>
<meta charset="utf-8">
<title>lumenfeldmedia – Briefpapier</title>
<link href="https://fonts.googleapis.com/css2?family=Roboto:wght@400;700&display=swap" rel="stylesheet">
<style>
  :root {
    --brand-blue: #00aeef;
    --brand-blue-light: #b5e5f8;
    --ink: #2b2b2d;
    --tab-dark: #3c3c3e;
    --paper: #ffffff;
    --backdrop: #ffffff;
  }
  * { margin: 0; padding: 0; box-sizing: border-box; }
  html, body {
    width: 878px; height: 1200px; overflow: hidden;
    background: var(--backdrop);
    font-family: "Roboto", Arial, sans-serif;
    color: var(--ink);
  }
  .sheet {
    position: absolute; left: 38px; top: 33px;
    width: 800px; height: 1130px;
    background: var(--paper);
    box-shadow: 0 0 6px rgba(0,0,0,0.35);
    overflow: hidden;
  }
  .top-band { position: absolute; left: 0; top: 0; }

  .wordmark {
    position: absolute; display: flex; align-items: center;
    font-weight: 400; white-space: nowrap;
  }
  .wordmark .dot {
    border-radius: 50%; border: 2px solid currentColor; flex: none;
  }
  .wordmark--header {
    right: 38px; top: 30px; font-size: 34px; color: var(--ink); gap: 8px;
    letter-spacing: -0.3px;
  }
  .wordmark--header .dot { width: 32px; height: 32px; border-color: var(--brand-blue); }

  .sender-line {
    position: absolute; left: 96px; top: 109px;
    font-size: 7.4px; padding-bottom: 2px;
    border-bottom: 1px solid var(--brand-blue);
    display: flex; align-items: center; gap: 3px;
  }
  .sender-line .dot { width: 8px; height: 8px; border-radius: 50%; border: 1px solid var(--brand-blue); }
  .sender-line strong { font-weight: 700; }

  .contact-block {
    position: absolute; left: 602px; top: 90px; width: 160px;
    font-size: 10.5px; line-height: 13px;
  }
  .contact-block .rule {
    height: 0; border-top: 2px dotted var(--brand-blue); margin: 4px 0 6px;
  }
  .contact-block .rule:first-child { margin-top: 0; }
  .contact-block strong { font-weight: 700; }

  .fold-mark { position: absolute; left: 6px; width: 14px; height: 0; border-top: 1px solid var(--brand-blue); }
  .fold-mark--upper { top: 332px; }
  .fold-mark--lower { top: 732px; }
  .punch-mark { position: absolute; left: 6px; top: 559px; }

  .tagline {
    position: absolute; left: 753px; top: 998px;
    transform: rotate(-90deg); transform-origin: 0 0;
    font-size: 24px; font-weight: 700; color: var(--brand-blue-light);
    white-space: nowrap; letter-spacing: 0.4px;
  }

  .footer-shapes { position: absolute; left: 0; top: 1010px; }
  .footer-circle {
    position: absolute; left: 43px; top: 1020px; width: 59px; height: 59px;
    border-radius: 50%; border: 3px solid var(--brand-blue);
  }
  .wordmark--tab {
    left: 604px; top: 1023px; font-size: 20px; color: #fff; gap: 5px;
  }
  .wordmark--tab .dot { width: 17px; height: 17px; border-width: 1.5px; }

  .footer-columns {
    position: absolute; top: 1062px; left: 0; width: 800px;
    color: #fff; font-size: 10.5px; line-height: 12.2px;
  }
  .footer-col { position: absolute; top: 0; }
  .footer-col strong { font-weight: 700; }
  .footer-col .gap { height: 12px; }
  .footer-col--address { left: 155px; }
  .footer-col--contact { left: 298px; }
  .footer-col--tax { left: 493px; }
  .footer-col--bank { left: 613px; }
  .footer-divider {
    position: absolute; top: 1059px; height: 62px; width: 0;
    border-left: 2px dotted rgba(255,255,255,0.85);
  }
</style>
</head>
<body>
<main class="sheet">
  <svg class="top-band" width="480" height="26" viewBox="0 0 480 26" aria-hidden="true">
    <path d="M0 0 H472 C462 8 455 20 440 26 H0 Z" fill="var(--brand-blue)"/>
  </svg>

  <div class="wordmark wordmark--header"><span class="dot"></span>lumenfeldmedia</div>

  <p class="sender-line"><span class="dot"></span><strong>lumenfeldmedia</strong> • Lindenallee 42 • 50999 Köln</p>

  <address class="contact-block" style="font-style:normal">
    <div class="rule"></div>
    <strong>lumenfeldmedia</strong><br>Jonas Kellermann<br>Lindenallee 42<br>50999 Köln
    <div class="rule"></div>
    Telefon: +49 221 000 482 17<br>E-Mail:&nbsp;&nbsp;info@lumenfeldmedia.de
    <div class="rule"></div>
    <strong>www.lumenfeldmedia.de</strong>
    <div class="rule"></div>
  </address>

  <span class="fold-mark fold-mark--upper"></span>
  <svg class="punch-mark" width="12" height="16" viewBox="0 0 12 16" aria-hidden="true">
    <path d="M2 1.5 L10 8 L2 14.5 Z" fill="none" stroke="var(--brand-blue)" stroke-width="1.5"/>
  </svg>
  <span class="fold-mark fold-mark--lower"></span>

  <p class="tagline">Veranstaltungstechnik - Medientechnik - Livestreaming</p>

  <svg class="footer-shapes" width="800" height="120" viewBox="0 0 800 120" aria-hidden="true">
    <path d="M598 9 H800 V38 H582 Z" fill="var(--tab-dark)"/>
    <path d="M82 120 L122 50 Q130 38 146 38 H800 V120 Z" fill="var(--brand-blue)"/>
  </svg>
  <span class="footer-circle"></span>
  <div class="wordmark wordmark--tab"><span class="dot"></span>lumenfeldmedia</div>

  <span class="footer-divider" style="left:277px"></span>
  <span class="footer-divider" style="left:472px"></span>
  <span class="footer-divider" style="left:592px"></span>

  <footer class="footer-columns">
    <div class="footer-col footer-col--address"><strong>lumenfeldmedia</strong><br>Jonas Kellermann<br>Lindenallee 42<br>50999 Köln</div>
    <div class="footer-col footer-col--contact">Telefon: +49 221 000 482 17<br>E-Mail:&nbsp;&nbsp;info@lumenfeldmedia.de<div class="gap"></div><strong>www.lumenfeldmedia.de</strong></div>
    <div class="footer-col footer-col--tax"><strong>Umsatzsteuer-Id</strong><br>DE000123456</div>
    <div class="footer-col footer-col--bank"><strong>Bankverbindung</strong><br>IBAN DE00111122223333444455<br>BIC BANKDEXX000<br>Stadtbank Köln</div>
  </footer>
</main>
</body>
</html>
```